Business Card Design

Great brand name mattresses at bulk prices, quality affordable for everyone.

something relating to a mattress is important for the card please.

Industry/Entity Type

Business

Contact Information for Business Card

Tervo Mattress

Requirements
Must have
• something related to a mattress, its the only thing we sell… the logo is not mandatory but would like, i understand the logo does not have a mattress

```html
<!DOCTYPE html>
<html lang="en">
<head>
<meta charset="utf-8">
<title>Tervo Mattress – Business Card</title>
<link rel="stylesheet" href="https://fonts.googleapis.com/css2?family=Arimo:wght@400;700&family=Roboto+Slab:wght@300;400;800&display=swap">
<style>
  :root {
    --backdrop: #d8d5d0;
    --card-white: #ffffff;
    --brand-yellow: #ffcb05;
    --brand-orange: #f28705;
    --ink: #1e1a17;
    --photo-light: #eeeeec;
    --photo-mid: #c9ccd0;
    --photo-dark: #9a9ea4;
  }
  * { margin: 0; padding: 0; box-sizing: border-box; }
  html, body { width: 1200px; height: 900px; overflow: hidden; }
  body {
    background: var(--backdrop);
    position: relative;
    font-family: "Roboto Slab", serif;
    color: var(--ink);
  }

  .card {
    position: absolute;
    left: 318px;
    width: 632px;
    height: 370px;
    overflow: hidden;
    background: var(--card-white);
  }
  .card--front { top: 58px; }
  .card--back { top: 470px; }

  /* Front */
  .front-art { position: absolute; inset: 0; }
  .front-wordmark {
    position: absolute;
    left: 364px;
    top: 136px;
    width: 250px;
    text-align: center;
    font-weight: 800;
    color: var(--ink);
    line-height: 1;
  }
  .front-wordmark .word-top { display: block; font-size: 60px; letter-spacing: 1px; }
  .front-wordmark .word-bottom { display: block; font-size: 40px; margin-top: 6px; letter-spacing: 0.5px; }

  .tag {
    position: absolute;
    background: var(--ink);
    font-family: "Roboto Slab", serif;
    font-weight: 400;
    white-space: nowrap;
    transform: rotate(-6deg);
    transform-origin: left center;
  }
  .tag--brands {
    left: 368px; top: 256px;
    padding: 4px 20px 6px;
    font-size: 26px;
    color: var(--brand-yellow);
  }
  .tag--offer {
    left: 433px; top: 306px;
    padding: 4px 22px 6px 40px;
    font-size: 22px;
    color: var(--card-white);
    transform: rotate(6deg);
  }

  /* Back */
  .back-wordmark {
    position: absolute;
    left: 70px;
    top: 20px;
    font-weight: 800;
    color: var(--ink);
    line-height: 1;
  }
  .back-wordmark .word-top { display: block; font-size: 58px; letter-spacing: 2px; }
  .back-wordmark .word-bottom { display: block; font-size: 43px; margin-top: 4px; }

  .rule {
    position: absolute;
    top: 109px;
    height: 3px;
    background: var(--brand-orange);
  }
  .rule--left { left: 0; width: 63px; }
  .rule--right { left: 320px; right: 0; }

  .people { position: absolute; left: 0; top: 152px; list-style: none; }
  .person {
    position: relative;
    height: 27px;
    padding-left: 69px;
    font-family: "Arimo", sans-serif;
    font-size: 15px;
    line-height: 18px;
  }
  .person::before {
    content: "";
    position: absolute;
    left: 0; top: 2px;
    width: 52px; height: 12px;
    background: var(--brand-orange);
  }
  .person-name { color: var(--brand-orange); font-weight: 700; margin-right: 4px; }
  .person-role { color: var(--ink); }

  .contacts {
    position: absolute;
    left: 70px;
    top: 229px;
    font-family: "Roboto Slab", serif;
    font-weight: 300;
    font-size: 14.5px;
    line-height: 20.5px;
    list-style: none;
  }
  .contact-group { margin-bottom: 0; }
  .contact-group--web { margin-top: 3px; }
  .contact-icon { position: absolute; left: -50px; }
  .contact-icon--home { top: 6px; }
  .contact-icon--phone { top: 49px; }
  .contact-icon--web { top: 91px; }
</style>
</head>
<body>

  <section class="card card--front" aria-label="Business card front">
    <svg class="front-art" width="632" height="370" viewBox="0 0 632 370">
      <defs>
        <linearGradient id="mattressTones" x1="0" y1="0" x2="0" y2="1">
          <stop offset="0" stop-color="var(--photo-light)"/>
          <stop offset="0.55" stop-color="var(--photo-mid)"/>
          <stop offset="0.7" stop-color="var(--photo-dark)"/>
          <stop offset="1" stop-color="var(--photo-light)"/>
        </linearGradient>
      </defs>
      <polygon points="0,0 370,0 322,370 0,370" fill="url(#mattressTones)" role="img" aria-label="Photo of a tall stack of white and grey mattresses"/>
      <polygon points="363,0 632,0 632,370 315,370" fill="var(--brand-orange)"/>
      <polygon points="374,0 632,0 632,370 326,370" fill="var(--brand-yellow)"/>
    </svg>
    <div class="front-wordmark">
      <span class="word-top">TERVO</span>
      <span class="word-bottom">MATTRESS</span>
    </div>
    <div class="tag tag--brands">Best Brands</div>
    <div class="tag tag--offer">75% OFF</div>
  </section>

  <section class="card card--back" aria-label="Business card back">
    <div class="back-wordmark">
      <span class="word-top">TERVO</span>
      <span class="word-bottom">MATTRESS</span>
    </div>
    <div class="rule rule--left"></div>
    <div class="rule rule--right"></div>

    <ul class="people">
      <li class="person"><span class="person-name">Mateo Rivas</span> <span class="person-role">President</span></li>
      <li class="person"><span class="person-name">Daniel Rivas</span> <span class="person-role">Manager</span></li>
    </ul>

    <ul class="contacts">
      <svg class="contact-icon contact-icon--home" width="34" height="30" viewBox="0 0 34 30" aria-hidden="true">
        <path d="M17 2 L1 16 H6 V29 H14 V20 H20 V29 H28 V16 H33 Z" fill="var(--brand-orange)"/>
      </svg>
      <svg class="contact-icon contact-icon--phone" width="30" height="30" viewBox="0 0 30 30" aria-hidden="true">
        <circle cx="15" cy="15" r="13" fill="none" stroke="var(--brand-orange)" stroke-width="2"/>
        <path d="M11 7 L14 10 L12 13 Q14 17 17 19 L20 17 L23 20 L20 23 Q13 22 8 12 Z" fill="var(--brand-orange)"/>
      </svg>
      <svg class="contact-icon contact-icon--web" width="30" height="30" viewBox="0 0 30 30" aria-hidden="true">
        <g fill="none" stroke="var(--brand-orange)" stroke-width="1.8">
          <circle cx="15" cy="15" r="13"/>
          <ellipse cx="15" cy="15" rx="6" ry="13"/>
          <line x1="2" y1="15" x2="28" y2="15"/>
          <line x1="15" y1="2" x2="15" y2="28"/>
          <path d="M4 8 H26 M4 22 H26"/>
        </g>
      </svg>
      <li class="contact-group">4210 SW, 212 Street, Unit 18, Tervo Bay, FL 30421<br>75 NW, 140 Street, Tervo Bay, FL 30428</li>
      <li class="contact-group">(555) 214 3087<br>(555) 386 0192</li>
      <li class="contact-group contact-group--web">info@tervobulkmattress.com<br>www.tervobulkmattress.com</li>
    </ul>
  </section>

</body>
</html>
```